Stylish Business Card for Modern hair salon

I need a simple business card design using our salon logo and colours that are in the logo. We service clients of all ages but predominantly those in the 18 to 55 age range. We have a young staff and are looking to have a card that will present a modern and clean image that represents who we are. The card should be in black and white same as our logo. Minimal use of other colours is allowed.

Industry/Entity Type

Hair And Beauty

Contact Information for Business Card

The design should have the following information
salon name - TZ Hair Studio
address - 2957 Fernbrook Rd.W. Mississauga, ON L8R3P2
phone - 905 641-2087
website - tzhairexample.ca
instagram - tz.hairstudio
twitter - @TZ_HairStudio

Colors
000000
ffffff
474747

Requirements
Must have
• simple design, salon name, address, phone, website, instagram, twitter info
• Back of card should have the following:
• YOUR NEXT APPOINTMENT
• DATE
• TIME
Nice to have
• simple design, clear to see and read,
• predominantly black and white colour, minimal use of other colours is ok
Should not have
• many colours, various fonts

```html
<!DOCTYPE html>
<html lang="en">
<head>
<meta charset="utf-8">
<title>TZ Hair Studio – Business Card</title>
<link href="https://fonts.googleapis.com/css2?family=Open+Sans:wght@400;600;700&display=swap" rel="stylesheet">
<style>
  :root {
    --ink: #000000;
    --paper: #ffffff;
    --grey: #474747;
    --stage: #d9d9d9;
    --rule: #8a8a8a;
  }
  * { box-sizing: border-box; margin: 0; padding: 0; }
  html, body { width: 1200px; height: 900px; overflow: hidden; }
  body {
    background: var(--stage);
    font-family: "Open Sans", Arial, sans-serif;
    color: var(--ink);
    display: flex;
    flex-direction: column;
    align-items: center;
    justify-content: center;
    gap: 60px;
  }
  .card {
    width: 630px;
    height: 360px;
    background: var(--paper);
    position: relative;
    overflow: hidden;
    box-shadow: 0 4px 14px rgba(0,0,0,0.18);
  }

  /* Appointment side */
  .wordmark {
    font-weight: 400;
    letter-spacing: 1px;
    text-align: center;
  }
  .appointment .wordmark {
    position: absolute;
    top: 42px; left: 0; right: 0;
    font-size: 44px;
    color: var(--ink);
  }
  .appointment-title {
    position: absolute;
    top: 138px; left: 0; right: 0;
    text-align: center;
    font-weight: 700;
    font-size: 18px;
    letter-spacing: 0.5px;
  }
  .field-rows {
    position: absolute;
    left: 48px; right: 48px; top: 200px;
    display: flex;
    flex-direction: column;
    gap: 34px;
  }
  .field-row { display: flex; align-items: flex-end; gap: 10px; }
  .field-label { font-size: 17px; white-space: nowrap; }
  .field-line {
    flex: 1;
    border-bottom: 2px dotted var(--rule);
    height: 18px;
  }
  .field-suffix { font-size: 11px; color: var(--grey); white-space: nowrap; }

  /* Contact side */
  .brand-band {
    position: absolute;
    top: 0; left: 0; right: 0;
    height: 190px;
    background: linear-gradient(135deg, #2a2a2a 0%, var(--ink) 60%);
    display: flex;
    align-items: center;
    justify-content: center;
  }
  .brand-band .wordmark { font-size: 50px; color: var(--paper); }
  .owner {
    position: absolute;
    left: 40px; bottom: 36px;
    font-size: 15px;
    line-height: 1.35;
    color: var(--grey);
  }
  .owner-name { font-weight: 700; color: var(--ink); font-size: 16px; }
  .contact-list {
    position: absolute;
    right: 36px; top: 212px;
    list-style: none;
    font-size: 14px;
    line-height: 1.5;
    text-align: right;
  }
  .contact-list li { display: flex; align-items: center; justify-content: flex-end; gap: 8px; }
  .contact-icon { width: 12px; height: 12px; flex: none; }
</style>
</head>
<body>

  <section class="card appointment">
    <div class="wordmark">TZ Hair Studio</div>
    <h2 class="appointment-title">YOUR NEXT APPOINTMENT</h2>
    <div class="field-rows">
      <div class="field-row">
        <span class="field-label">Name:</span><span class="field-line"></span>
      </div>
      <div class="field-row">
        <span class="field-label">Date:</span><span class="field-line"></span>
        <span class="field-label">Time:</span><span class="field-line"></span>
        <span class="field-suffix">AM/PM</span>
      </div>
    </div>
  </section>

  <section class="card contact">
    <div class="brand-band">
      <div class="wordmark">TZ Hair Studio</div>
    </div>
    <ul class="contact-list">
      <li>905 641-2087
        <svg class="contact-icon" viewBox="0 0 12 12"><path d="M2.5 1 L4.5 1 L5.2 3.6 L3.9 4.6 Q5 7 7.4 8.1 L8.4 6.8 L11 7.5 L11 9.5 Q10.5 11 9 11 Q1 10 1 3 Q1 1.5 2.5 1 Z" fill="var(--ink)"/></svg>
      </li>
      <li>www.tzhairexample.ca
        <svg class="contact-icon" viewBox="0 0 12 12"><circle cx="6" cy="6" r="5.5" fill="var(--ink)"/></svg>
      </li>
      <li>@TZ_HairStudio
        <svg class="contact-icon" viewBox="0 0 12 12"><circle cx="6" cy="6" r="5.5" fill="var(--ink)"/></svg>
      </li>
      <li>tz.hairstudio
        <svg class="contact-icon" viewBox="0 0 12 12"><rect x="0.5" y="0.5" width="11" height="11" rx="2" fill="var(--ink)"/></svg>
      </li>
    </ul>
    <address class="owner" style="font-style:normal">
      <div class="owner-name">ALEX MORENO</div>
      <div>CEO/FOUNDER</div>
      <div>2957 Fernbrook Rd.W.</div>
      <div>Mississauga, ON L8R3P2</div>
    </address>
  </section>

</body>
</html>
```